Tall Pine Backcountry Hunting Lodge Website Design

Our client Tall Pine Backcountryy would like us to design a website. Their services are similar to Copper Hollow Ranch (https://seecopperhollow.com).

We prefer using Adobe Fonts in the design. Please keep track of images/icons used in the design. We plan on purchasing the images used in your design.

Number of Pages Required

1 page

Font styles to use
Sans Serif

Colors
0054AA
0677BA
7BADD7
CADEEF
E8F1F8

```html
<!DOCTYPE html>
<html lang="en">
<head>
<meta charset="utf-8">
<title>Tall Pine Backcountry Hunting Lodge</title>
<link rel="stylesheet" href="https://fonts.googleapis.com/css2?family=Montserrat:wght@400;500;600;700;800&display=swap">
<style>
:root{
  --navy:#16426a;
  --navy-tile:#2c5982;
  --navy-dark:#0f3152;
  --gold:#f2a81d;
  --gold-soft:#f6bd45;
  --ink:#1f2a36;
  --paper:#ffffff;
  --mist:#e8f1f8;
  --black:#050505;
}
*{margin:0;padding:0;box-sizing:border-box}
html,body{width:1200px;height:5338px;overflow:hidden}
body{position:relative;font-family:'Montserrat',sans-serif;color:var(--ink);background:var(--paper)}
.abs{position:absolute}
.photo{position:absolute;display:block}
.btn{position:absolute;display:flex;align-items:center;justify-content:center;font-size:10px;font-weight:700;letter-spacing:.5px;text-transform:uppercase}
.btn-navy{background:var(--navy);color:#fff;border-bottom:3px solid var(--gold)}
.btn-gold{background:var(--gold);color:var(--navy);border-bottom:3px solid #d48e0d}
.btn-white{background:#fff;color:var(--navy);border-bottom:3px solid var(--gold)}
.h2{position:absolute;left:0;width:1200px;text-align:center;font-weight:700;font-size:42px;letter-spacing:-.5px}
.rule{position:absolute;left:570px;width:60px;height:3px;background:var(--gold)}
.lead{position:absolute;text-align:center;font-size:11px;line-height:20px}

/* header */
.site-header{position:absolute;left:0;top:0;width:1200px;height:77px;background:#fff;border-top:3px solid var(--gold);z-index:3}
.nav-link{position:absolute;top:33px;font-size:10px;font-weight:500;letter-spacing:2px;color:var(--navy);text-transform:uppercase}
.nav-link .caret{display:block;text-align:center;font-size:7px;margin-top:8px}
.brand-badge{position:absolute;left:520px;top:0;width:160px;height:128px;background:#fff;clip-path:polygon(0 0,100% 0,100% 78%,50% 100%,0 78%);z-index:4;display:flex;flex-direction:column;align-items:center;justify-content:center}
.brand-name{font-weight:800;font-size:15px;color:var(--navy);text-align:center;line-height:17px;letter-spacing:.5px}
.brand-sub{font-size:6px;font-weight:700;letter-spacing:3px;color:var(--navy);margin-top:3px}

/* hero */
.hero-title{position:absolute;left:0;top:196px;width:1200px;text-align:center;font-weight:700;font-size:52px;line-height:58px;color:var(--navy);letter-spacing:-.5px}
.hero-copy{position:absolute;left:197px;top:532px;width:290px;font-size:10.5px;line-height:15px;color:#fff}
.discover{position:absolute;left:96px;top:575px;transform:rotate(-90deg);transform-origin:left top;font-size:9px;font-weight:600;letter-spacing:1px;color:#fff;white-space:nowrap}
.plan-card{position:absolute;left:607px;top:522px;width:394px;height:361px;background:var(--gold);z-index:2}
.plan-card h3{position:absolute;top:30px;width:100%;text-align:center;color:#fff;font-size:15px;font-weight:700}
.field{position:absolute;left:52px;width:292px;height:29px;background:var(--gold-soft);border:1px solid #f8ce6e;color:#fff;font-size:8px;font-weight:600;padding:8px 14px}
.send{position:absolute;left:307px;top:286px;width:33px;height:29px;background:var(--navy);display:flex;align-items:center;justify-content:center}

/* about */
.about-frame{position:absolute;left:197px;top:852px;width:410px;height:531px;border:8px solid #f9ef9a;box-shadow:0 10px 30px rgba(0,0,0,.15)}
.about-title{position:absolute;left:711px;top:980px;font-size:42px;font-weight:700;color:var(--navy)}
.about-copy{position:absolute;left:711px;top:1061px;width:295px;font-size:10.5px;line-height:18.6px;color:#333}

/* western */
.western{position:absolute;left:0;top:1478px;width:1200px;height:867px;background:var(--navy)}
.tab{position:absolute;top:257px;width:155px;height:139px;background:var(--navy-tile);color:#fff;font-size:8.5px;font-weight:700;text-align:center;line-height:12px;display:flex;flex-direction:column;align-items:center;justify-content:center;gap:12px}
.tab.is-active{background:#fff;color:var(--navy)}
.float-card{position:absolute;left:746px;top:479px;width:255px;height:288px;background:var(--gold);color:#fff;text-align:center}

/* winter */
.winter{position:absolute;left:0;top:2345px;width:1200px;height:624px}
.pack{position:absolute;top:273px;width:355px;height:259px;color:#fff}
.pack h4{position:absolute;left:32px;top:112px;font-size:17px;font-weight:700}
.pack p{position:absolute;left:32px;top:142px;width:290px;font-size:11px;line-height:18px}
.pack .more{position:absolute;left:32px;top:211px;font-size:13px;font-weight:700}

/* testimonials */
.testi{position:absolute;left:0;top:4333px;width:1200px;height:532px;background:var(--navy)}
.quote-card{position:absolute;left:240px;top:188px;width:718px;height:208px;background:linear-gradient(180deg,#fff,#eef2f5);border-radius:8px;text-align:center}
.arrow{position:absolute;top:276px;width:60px;height:40px}

/* footer */
.footer{position:absolute;left:0;top:4865px;width:1200px;height:473px;background:var(--black);color:#fff}
.foot-head{position:absolute;top:245px;font-size:10px;font-weight:700;letter-spacing:.5px}
.foot-link{position:absolute;font-size:8.5px;letter-spacing:.5px}
.social{position:absolute;top:332px;width:30px;height:30px;border-radius:50%;border:2px solid #fff}
</style>
</head>
<body>

<!-- header -->
<header class="site-header">
  <a class="nav-link" style="left:196px">Summer Trips<span class="caret">▼</span></a>
  <a class="nav-link" style="left:376px">Lodging</a>
  <a class="nav-link" style="left:762px">Info<span class="caret">▼</span></a>
  <a class="nav-link" style="left:880px">Shop</a>
  <a class="btn btn-navy" style="left:1002px;top:22px;width:124px;height:33px;font-size:9px">Contact</a>
</header>
<div class="brand-badge">
  <div class="brand-name">TALL PINE<br>BACKCOUNTRY</div>
  <div class="brand-sub">HUNTING LODGE</div>
</div>

<!-- hero -->
<section class="hero">
  <div class="photo" role="img" aria-label="Mountain valley at dusk with pine forest and a distant lodge" style="left:0;top:77px;width:1200px;height:682px;background:linear-gradient(180deg,#b9c3c8 0%,#d7cdb4 30%,#8a8a5a 48%,#3f4a22 62%,#1a1f12 85%,#0d0f09 100%)"></div>
  <h1 class="hero-title">YOUR LIFE<br>CHANGING JOURNEY<br>BEGINS</h1>
  <div class="rule" style="top:377px;left:568px;width:64px"></div>
  <p class="hero-copy">Lorem Ipsum is simply dummy text of the printing and typesetting industry. Lorem Ipsum has been the industry's standard dummy text ever since the 1500s, when an unknown printer took a galley of type and scrambled it.</p>
  <a class="btn btn-gold" style="left:197px;top:640px;width:145px;height:30px">View Lodging</a>
  <div class="discover">DISCOVER NOW</div>
  <svg class="abs" style="left:100px;top:632px" width="10" height="30" viewBox="0 0 10 30"><path d="M5 0V28M1 24L5 29L9 24" stroke="#fff" stroke-width="1.2" fill="none"/></svg>
  <div class="abs" style="left:131px;top:497px;width:2px;height:328px;background:var(--gold)"></div>

  <form class="plan-card">
    <h3>PLAN YOUR TRIP</h3>
    <div class="field" style="top:75px">Name</div>
    <div class="field" style="top:114px">Email address</div>
    <div class="field" style="top:152px">Phone no.</div>
    <div class="field" style="top:189px;height:129px">Message...</div>
    <div class="send"><svg width="14" height="14" viewBox="0 0 14 14"><path d="M1 7L13 1L9 13L7 8Z" fill="#fff"/></svg></div>
  </form>
</section>

<!-- about -->
<section class="about">
  <div class="about-frame photo" role="img" aria-label="Two horses grazing below an autumn mountain with a wooden cabin" style="background:linear-gradient(180deg,#3c4048 0%,#7f8684 22%,#a46a2e 42%,#6f7a34 60%,#3d5a25 80%,#506b2a 100%)"></div>
  <h2 class="about-title">ABOUT US</h2>
  <div class="rule" style="left:711px;top:1035px;width:0"></div>
  <p class="about-copy">Lorem Ipsum is simply dummy text of the printing and typesetting industry. Lorem Ipsum has been the industry's standard dummy text ever since the 1500s, when an unknown printer took a galley of type and scrambled it to make a type specimen book. It has survived not only five centuries, but also the leap into electronic typesetting, remaining essentially unchanged. It was popularised in the 1960s with the release of Letraset sheets containing Lorem Ipsum passages, and more recently with desktop layout tools including versions of Lorem Ipsum.</p>
  <a class="btn btn-navy" style="left:711px;top:1314px;width:122px;height:31px">Contact</a>
</section>

<!-- western -->
<section class="western">
  <h2 class="h2" style="top:85px;color:#fff">WESTERN MT VACATIONS</h2>
  <p class="lead" style="left:190px;top:168px;width:820px;color:#fff">Lorem Ipsum is simply dummy text of the printing and typesetting industry. Lorem Ipsum has been the industry's standard dummy text ever since the 1500s, when an unknown printer took a galley of type and scrambled it to make a type specimen book.</p>

  <div class="tab is-active" style="left:197px">
    <svg width="34" height="34" viewBox="0 0 34 34"><circle cx="17" cy="17" r="12" fill="none" stroke="var(--gold)" stroke-width="2"/><path d="M8 17H26M17 8V26" stroke="var(--gold)" stroke-width="2"/></svg>
    <span>RIVER<br>RAFTING</span></div>
  <div class="tab" style="left:359px">
    <svg width="34" height="34" viewBox="0 0 34 34"><path d="M4 24H30M8 24L12 14H24L28 24M14 14L16 9H22" fill="none" stroke="#fff" stroke-width="2"/></svg>
    <span>SNOWMOBILE<br>RENTALS</span></div>
  <div class="tab" style="left:521px">
    <svg width="34" height="34" viewBox="0 0 34 34"><path d="M5 16L17 6L29 16V29H5Z M13 29V20H21V29" fill="none" stroke="#fff" stroke-width="2"/></svg>
    <span>LODGING</span></div>
  <div class="tab" style="left:683px">
    <svg width="34" height="34" viewBox="0 0 34 34"><path d="M6 17C12 9 22 9 28 17C22 25 12 25 6 17Z M28 17L32 12V22Z" fill="none" stroke="#fff" stroke-width="2"/></svg>
    <span>FISHING TRIPS</span></div>
  <div class="tab" style="left:845px">
    <svg width="34" height="34" viewBox="0 0 34 34"><path d="M4 22Q10 18 17 22T30 22M6 27Q12 23 17 27T30 27M17 6V18M12 12L17 6L22 12" fill="none" stroke="#fff" stroke-width="2"/></svg>
    <span>RIVER<br>RAFTING</span></div>

  <div class="abs" style="left:197px;top:433px;width:804px;height:1px;background:#3e6892"></div>
  <svg class="abs" style="left:266px;top:434px" width="16" height="8" viewBox="0 0 16 8"><path d="M0 0H16L8 8Z" fill="#3e6892"/></svg>

  <div class="photo" role="img" aria-label="Group of friends paddling a yellow raft through white water" style="left:197px;top:479px;width:255px;height:288px;background:linear-gradient(160deg,#d9dcd8,#8b8f7d 40%,#d2b43a 65%,#3c4a55)"></div>
  <div class="photo" role="img" aria-label="Kayaker paddling through a rushing river" style="left:473px;top:479px;width:255px;height:288px;background:linear-gradient(170deg,#6b7677,#9ea7a3 40%,#4f6a4f 70%,#c8d0cc)"></div>
  <div class="float-card">
    <h4 style="position:absolute;top:72px;width:100%;font-size:15px;font-weight:700">RIVER FLOAT TRIPS</h4>
    <p style="position:absolute;left:50px;top:108px;width:155px;font-size:8.5px;line-height:14px">Floating with a friend or your family is a great way to enjoy the St. Regis River! It provides you the perfect getaway with no distractions.</p>
    <span style="position:absolute;left:0;top:205px;width:100%;font-size:10px;font-weight:700">SEE NOW &nbsp;⟶</span>
  </div>
</section>

<!-- winter -->
<section class="winter">
  <div class="photo" role="img" aria-label="Dark snowy pine forest with people walking along a trail" style="left:0;top:0;width:1200px;height:624px;background:linear-gradient(180deg,#1d2324 0%,#2f3534 35%,#5b6366 70%,#7b8386 100%)"></div>
  <h2 class="h2" style="top:92px;color:#fff">WINTER VACATION PACKAGES</h2>
  <div class="rule" style="top:155px"></div>
  <p class="lead" style="left:300px;top:177px;width:600px;color:#fff">Choose what suits your style. Copper Hollow Ranch offers a variety of Montana vacation options to satisfy the needs of your family and friends of all ages and abilities.</p>

  <div class="pack" style="left:232px">
    <div class="photo" role="img" aria-label="Snow-covered forest in blue winter light" style="inset:0;background:linear-gradient(160deg,#9fb3c4,#6b89a6 50%,#3e5f80)"></div>
    <h4>MT. VACATIONS</h4>
    <p>Give your family a lifetime of memories with a vacation in western Montana.</p>
    <span class="more">MONTANNA VACATIONS &nbsp;⟶</span>
  </div>
  <div class="pack" style="left:612px">
    <div class="photo" role="img" aria-label="Angler on a boat holding up a fresh catch" style="inset:0;background:linear-gradient(160deg,#b6c3d1,#7d91a9 50%,#3c5578)"></div>
    <h4>MT. FISHING TRIPS</h4>
    <p>Learn to fly fish and relax like never before with our expert guides.</p>
    <span class="more">FISHING TRIPS &nbsp;⟶</span>
  </div>
</section>

<!-- photo of the day -->
<section class="gallery">
  <h2 class="h2" style="top:3045px;color:var(--navy)">PHOTO OF THE DAY!</h2>
  <div class="rule" style="top:3105px"></div>
  <div class="photo" role="img" aria-label="Snowmobile on a snowy field by frosted trees" style="left:197px;top:3145px;width:462px;height:373px;background:linear-gradient(180deg,#c9d8e6,#e9f0f6 45%,#dfe6ee 80%,#b8c2cc)"></div>
  <div class="photo" role="img" aria-label="Cabins on a green slope beneath a mountain peak" style="left:678px;top:3145px;width:323px;height:373px;background:linear-gradient(180deg,#d9e1e4,#7d8c8e 40%,#4f6a4a 70%,#6b8a3a)"></div>
  <div class="photo" role="img" aria-label="Motocross rider jumping at sunset" style="left:197px;top:3536px;width:274px;height:268px;background:linear-gradient(180deg,#b9b6ad,#cf9a62 55%,#6a4a30)"></div>
  <div class="photo" role="img" aria-label="Wooden lodge kitchen with bar stools" style="left:489px;top:3536px;width:274px;height:268px;background:linear-gradient(160deg,#8a4a1e,#c07a3a 50%,#5b2d12)"></div>
  <div class="photo" role="img" aria-label="Red A-frame cabin among pine trees" style="left:784px;top:3536px;width:217px;height:268px;background:linear-gradient(160deg,#d9e0e3,#b3372c 45%,#6b8a3e 80%)"></div>
  <div class="photo" role="img" aria-label="Hands holding a spotted brown trout" style="left:197px;top:3823px;width:323px;height:373px;background:linear-gradient(160deg,#5d7548,#c8a46d 50%,#a88a3c 75%,#4e5e3a)"></div>
  <div class="photo" role="img" aria-label="Hand releasing a trout into green water" style="left:539px;top:3823px;width:462px;height:373px;background:linear-gradient(160deg,#7f9693,#51706c 50%,#c7cfcb 70%,#3e5752)"></div>
  <a class="btn btn-navy" style="left:524px;top:4227px;width:150px;height:31px">See More</a>
</section>

<!-- testimonials -->
<section class="testi">
  <h2 class="h2" style="top:76px;color:#fff">TESTIMONIALS</h2>
  <div class="rule" style="top:136px"></div>
  <svg class="arrow" style="left:152px" viewBox="0 0 60 40"><circle cx="36" cy="20" r="18" fill="none" stroke="var(--gold)" stroke-width="1.2"/><path d="M4 20H50M12 13L4 20L12 27" fill="none" stroke="#fff" stroke-width="1.5"/></svg>
  <svg class="arrow" style="left:988px" viewBox="0 0 60 40"><circle cx="24" cy="20" r="18" fill="none" stroke="var(--gold)" stroke-width="1.2"/><path d="M10 20H56M48 13L56 20L48 27" fill="none" stroke="#fff" stroke-width="1.5"/></svg>
  <div class="quote-card">
    <h3 style="position:absolute;top:42px;width:100%;font-size:20px;font-weight:600;color:var(--navy);letter-spacing:.5px">Marta Kessler</h3>
    <p style="position:absolute;left:80px;top:96px;width:558px;font-size:9px;line-height:18px;color:#333">Lorem Ipsum ist einfach Blindtext der Druck- und Satzindustrie. Lorem Ipsum ist seit den 1500er Jahren der Standard-Dummy-Text der Branche, als ein unbekannter Drucker eine Reihe von Typen nahm und daraus ein Musterbuch für Typen erstellte. Sie hat nicht nur fünf Jahrhunderte, sondern auch den Sprung in den elektronischen.</p>
    <div style="position:absolute;top:160px;width:100%;font-size:11px;color:var(--gold);letter-spacing:2px">★★★★★</div>
  </div>
  <a class="btn btn-white" style="left:521px;top:429px;width:157px;height:31px">See More</a>
</section>

<!-- footer -->
<footer class="footer">
  <div style="position:absolute;left:0;top:100px;width:1200px;text-align:center">
    <div style="font-size:20px;font-weight:800;letter-spacing:1px">TALL PINE BACKCOUNTRY</div>
    <div style="font-size:8px;font-weight:700;letter-spacing:5px;margin-top:6px">HUNTING LODGE</div>
  </div>
  <p class="foot-link" style="left:197px;top:236px;width:200px;line-height:18px;letter-spacing:0">lorem ipsum is simply dummy text of the printing and typesetting industry. lorem ipsum has been the industry's standard dummy text ever since the 1500s.</p>
  <span class="social" style="left:197px"></span>
  <span class="social" style="left:238px"></span>
  <span class="social" style="left:279px"></span>
  <span class="social" style="left:320px"></span>

  <h5 class="foot-head" style="left:556px">USEFUL LINKS</h5>
  <a class="foot-link" style="left:556px;top:274px">SUMMER TRIPS</a>
  <a class="foot-link" style="left:556px;top:297px">LODGING</a>
  <a class="foot-link" style="left:556px;top:320px">INFO</a>
  <a class="foot-link" style="left:556px;top:343px">SHOP</a>

  <h5 class="foot-head" style="left:808px">CONTACT INFO</h5>
  <svg class="abs" style="left:808px;top:270px" width="16" height="16" viewBox="0 0 16 16"><circle cx="8" cy="8" r="8" fill="var(--navy-tile)"/><path d="M8 4A2.5 2.5 0 0 1 10.5 6.5C10.5 8.5 8 12 8 12S5.5 8.5 5.5 6.5A2.5 2.5 0 0 1 8 4Z" fill="#fff"/></svg>
  <span class="foot-link" style="left:840px;top:274px">LOREM IPSUM IS A DUMMY TEXT</span>
  <svg class="abs" style="left:808px;top:302px" width="16" height="16" viewBox="0 0 16 16"><circle cx="8" cy="8" r="8" fill="var(--navy-tile)"/><path d="M4 8L12 4L10 12L8 9Z" fill="#fff"/></svg>
  <span class="foot-link" style="left:840px;top:306px">LOREM IPSUM IS A DUMMY TEXT</span>
  <svg class="abs" style="left:808px;top:334px" width="16" height="16" viewBox="0 0 16 16"><circle cx="8" cy="8" r="8" fill="var(--navy-tile)"/><path d="M5 4L7 4L8 6.5L6.8 7.5Q7.8 9.5 9 10.2L10 9L12 10V12Q7 12 5 7Z" fill="#fff"/></svg>
  <span class="foot-link" style="left:840px;top:338px">LOREM IPSUM IS A DUMMY TEXT</span>

  <div class="abs" style="left:190px;top:400px;width:820px;height:1px;background:#333"></div>
  <p class="foot-link" style="left:0;top:432px;width:1200px;text-align:center;font-size:7.5px">COPYRIGHT © 2023 TALL PINE BACKCOUNTRY. ALL RIGHTS RESERVED.</p>
</footer>

</body>
</html>
```